Brookvale Strategy Partners Website Design

I need a website design for my new business consulting and executive coaching firm, Brookvale Strategy Partners. We provide consultative services to business C-suites as well as personal coaching to executives. I have attached the logo with color scheme I have chosen. I would like the website to reflect professionalism and continue the color scheme in the logo.

Target Market(s)

Small to medium business and their executives; middle to upper income men and women in mid- to late career looking for significance

Industry/Entity Type

Business Consultant

Number of Pages Required

4 page

Requirements
Must have
• A homepage with prominent logo and way to contact for more information; an area on the homepage with easy to read, clear text to describe what the company does; a prominent area on the homepage for a tagline; a blog page that can be updated regularly, an "about us" page with biographical information; an "about us" page; a page detailing services offered
• The web design must match the logo colors and font that I have uploaded.
Nice to have
• A lighthouse picture in the background or header
Should not have
• A lot of text area on the homepage

```html
<!DOCTYPE html>
<html lang="en">
<head>
<meta charset="utf-8">
<title>Brookvale Strategy Partners</title>
<link rel="stylesheet" href="https://fonts.googleapis.com/css2?family=Roboto+Condensed:wght@400&family=Tinos&family=Libre+Baskerville:wght@700&family=Arimo&display=swap">
<style>
:root{
  --navy:#1c2c5e;
  --maroon:#701010;
  --nav-red:#7a1414;
  --grey-btn:#666666;
  --ring:#c9c9c9;
  --ink:#111111;
  --card-line:#e6e6e6;
  --white:#ffffff;
  --hero-light:#f6f6f4;
  --hero-mid:#eef0ea;
  --hero-warm:#f2e9e3;
}
*{margin:0;padding:0;box-sizing:border-box}
html,body{width:1200px;height:825px;overflow:hidden;background:var(--white)}
.page{position:relative;width:1200px;height:825px;overflow:hidden;font-family:"Arimo",Arial,sans-serif;color:var(--ink)}
.hero-photo{position:absolute;left:0;top:130px;width:1200px;height:650px;
  background:linear-gradient(90deg,var(--white) 0%,var(--hero-light) 35%,var(--hero-mid) 58%,var(--hero-warm) 72%,var(--hero-light) 100%)}
.brand{position:absolute;left:164px;top:58px;display:flex;align-items:center;gap:8px;text-decoration:none}
.brand-mark{width:14px;height:14px;background:var(--navy)}
.brand-name{font-family:"Tinos",serif;font-size:15px;color:var(--navy);letter-spacing:.5px;text-transform:uppercase}
.phone{position:absolute;left:879px;top:21px;display:flex;align-items:center;gap:15px;font-family:"Roboto Condensed",sans-serif;font-size:20px;letter-spacing:.5px}
.main-nav{position:absolute;left:579px;top:69px;display:flex;font-family:"Tinos",serif;font-size:15px}
.main-nav a{color:var(--nav-red);text-decoration:none;height:23px;line-height:23px;padding:0 13px;margin-right:19px}
.main-nav a.current{background:var(--navy);color:var(--white);margin-right:23px}
.main-nav a:last-child{margin-right:0}
.tagline{position:absolute;left:0;top:235px;width:610px;text-align:center;font-family:"Libre Baskerville",serif;font-size:38px;line-height:46px;letter-spacing:-1px;text-shadow:1px 2px 2px rgba(0,0,0,.35)}
.card{position:absolute;top:587px;width:272px;height:193px;background:rgba(255,255,255,.8);border:1px solid var(--card-line);border-bottom:0;text-align:center}
.card-about{left:160px;background:var(--white)}
.card-services{left:464px}
.card-inquiry{left:768px}
.badge{position:absolute;left:76px;top:-79px;width:120px;height:120px;border-radius:50%;border:4px solid var(--ring);display:flex;align-items:center;justify-content:center}
.badge-inner{width:112px;height:112px;border-radius:50%;background:var(--navy);display:flex;align-items:center;justify-content:center}
.badge-maroon{background:#72100f;border:3px solid var(--navy)}
.card h2{position:absolute;left:0;right:0;top:54px;font-family:"Roboto Condensed",sans-serif;font-weight:400;font-size:19.5px}
.card p{position:absolute;left:14px;right:14px;top:83px;font-size:11.5px;line-height:18.5px}
.btn{position:absolute;left:84px;top:147px;height:31px;display:flex;align-items:center;color:var(--white);font-size:13px;text-decoration:none;filter:drop-shadow(1px 2px 1px rgba(0,0,0,.3))}
.btn span{background:var(--grey-btn);height:31px;line-height:31px;padding:0 8px;border-radius:3px 0 0 3px}
.btn i{width:0;height:0;border-top:15.5px solid transparent;border-bottom:15.5px solid transparent;border-left:14px solid var(--grey-btn)}
.btn-primary span{background:var(--navy)}
.btn-primary i{border-left-color:var(--navy)}
.site-footer{position:absolute;left:0;top:780px;width:1200px;height:45px;background:var(--maroon);color:var(--white)}
.follow{position:absolute;left:175px;top:0;height:45px;display:flex;align-items:center;gap:7px;font-family:"Roboto Condensed",sans-serif;font-size:15px}
.follow-label{margin-right:4px}
.social{width:28px;height:28px;border-radius:50%;background:var(--white);display:block}
.copyright{position:absolute;right:163px;top:0;line-height:45px;font-size:12.5px}
</style>
</head>
<body>
<div class="page">
  <div class="hero-photo" role="img" aria-label="Photo of a hand holding a light bulb with a small green tree growing inside, with plain white light bulbs floating around it"></div>

  <header>
    <a class="brand" href="#"><span class="brand-mark"></span><span class="brand-name">Brookvale Strategy Partners</span></a>
    <div class="phone">
      <svg width="34" height="34" viewBox="0 0 34 34" aria-hidden="true">
        <circle cx="17" cy="17" r="15.5" fill="none" stroke="var(--navy)" stroke-width="2"/>
        <path d="M13 9c-2 1-3 3-2 6 1 4 4 8 7 10 2 1 4 0 5-2l-3-3-2 1c-2-1-4-4-4-6l2-1-1-4z" fill="var(--navy)"/>
      </svg>
      <span>123-456-7890</span>
    </div>
    <nav class="main-nav">
      <a class="current" href="#">HOME</a>
      <a href="#">ABOUT US</a>
      <a href="#">SERVICES</a>
      <a href="#">BLOG</a>
      <a href="#">CONTACT US</a>
    </nav>
  </header>

  <h1 class="tagline">Are You Effectively<br>Reaching Your Customers?</h1>

  <section class="card card-about">
    <div class="badge badge-maroon"></div>
    <h2>About Us</h2>
    <p>Lorem ipsum dolor sit amet, consectetuer into euismod tincidunt ut laoreet dolore magnain aliquam erat volutpat.</p>
    <a class="btn btn-primary" href="#"><span>READ MORE</span><i></i></a>
  </section>

  <section class="card card-services">
    <div class="badge"><div class="badge-inner"></div></div>
    <h2>Services We Provide</h2>
    <p>Lorem ipsum dolor sit amet, consectetuer into euismod tincidunt ut laoreet dolore magnain aliquam erat volutpat.</p>
    <a class="btn" href="#"><span>READ MORE</span><i></i></a>
  </section>

  <section class="card card-inquiry">
    <div class="badge"><div class="badge-inner">
      <svg width="56" height="56" viewBox="0 0 34 34" aria-hidden="true">
        <circle cx="17" cy="17" r="15.5" fill="none" stroke="var(--white)" stroke-width="1.6"/>
        <path d="M13 9c-2 1-3 3-2 6 1 4 4 8 7 10 2 1 4 0 5-2l-3-3-2 1c-2-1-4-4-4-6l2-1-1-4z" fill="none" stroke="var(--white)" stroke-width="1.4"/>
      </svg>
    </div></div>
    <h2>QUICK INQUIRY</h2>
    <p>Lorem ipsum dolor sit amet, consectetuer into euismod tincidunt ut laoreet dolore magnain aliquam erat volutpat.</p>
    <a class="btn" href="#"><span>GET STARTED</span><i></i></a>
  </section>

  <footer class="site-footer">
    <div class="follow">
      <span class="follow-label">FOLLOW US</span>
      <a class="social" href="#" aria-label="Social profile 1"></a>
      <a class="social" href="#" aria-label="Social profile 2"></a>
      <a class="social" href="#" aria-label="Social profile 3"></a>
      <a class="social" href="#" aria-label="Social profile 4"></a>
    </div>
    <div class="copyright">© 2016 Brookvale Strategy Partners All Rights Reserved</div>
  </footer>
</div>
</body>
</html>
```